Flyer für Selbstwert-Coachin und Bewusstseinstrainerin
Der Flyer ist wunderschön, kreativ und edel geworden und wurde von der Designerin genau nach meinen Wünschen super umgesetzt! Ich bin sehr zufrieden und kann die Designerin Lunea2281 jedem nur empfehlen. Einfach Top!!! 1 A!!! Vielen herzlichen Dank!
Zielgruppe
Ich bin Selbstwert Coach und Bewusstseinstrainerin und möchte einen Flyer für mein neues Angebot 'Innenkraft Akademie für Jugendliche ab 16' gestalten lassen.
Die Zielgruppe sind Eltern von Jugendlichen in der Oberstufe, deren Kinder unter Schulstress und Leistungsdruck leiden und zu wenig Selbstbewusstsein haben.
Aufgabenstellung
Ich habe bereits das Titelbild bei Bildquell gesucht #739201584, bitte dieses nehmen, es kann auch ein ähnliches noch besseres vorgeschlagen werden.
Ich möchte einen ansprechenden, schönen, hochwertigen Flyer mit den Farben der Landingpage, gelb, blau, gold... und Bilder von Jugendlichen, dort wo Platz ist, ansprechend und klar. Bitte keine Schnörkel und 08 15 Figuren, das Auge soll hängen bleiben, der Flyer hängt straßenseitig. Dieser soll ein 6-seitiger Wickelfalz sein.

```html
<!DOCTYPE html>
<html lang="de">
<head>
<meta charset="utf-8">
<title>Innenkraft Akademie – Flyer</title>
<link href="https://fonts.googleapis.com/css2?family=Bebas+Neue&family=Open+Sans:ital,wght@0,400;0,600;0,700;1,400&display=swap" rel="stylesheet">
<style>
:root{
  --navy:#15126b;
  --yellow:#f7c600;
  --gold:#f2b705;
  --ink:#2c2c3a;
  --stage:#e6e6e6;
  --paper:#ffffff;
}
*{margin:0;padding:0;box-sizing:border-box}
html,body{width:847px;height:1200px;overflow:hidden;background:var(--stage)}
body{position:relative;font-family:"Open Sans",Arial,sans-serif;color:var(--ink)}
.sheet{position:absolute;left:83px;width:697px;height:495px;background:var(--paper);box-shadow:0 0 0 1px #d4d4d4}
.sheet--outer{top:135px}
.sheet--inner{top:660px}
.panel{position:absolute;top:0;height:100%;width:232px;overflow:hidden}
.panel--1{left:0}
.panel--2{left:233px;border-left:1px solid #e4e4e4;border-right:1px solid #e4e4e4}
.panel--3{left:465px}
.photo{position:absolute;left:0;width:100%}
.heading{font-family:"Bebas Neue",Impact,sans-serif;font-weight:400;color:var(--navy);letter-spacing:.3px;line-height:1}
.body{font-size:7.6px;line-height:1.42}
.body p{margin-bottom:5px}
.abs{position:absolute}
.ticks{list-style:none}
.ticks li{position:relative;padding-left:12px;margin-bottom:4px;font-size:7.6px;line-height:1.38}
.ticks svg{position:absolute;left:0;top:1px;width:10px;height:9px}
.gold-strip{position:absolute;left:0;width:100%;background:linear-gradient(90deg,var(--gold),#fde27a 60%,#fff6cf)}
.navy-band{position:absolute;left:0;width:100%;background:var(--navy)}
.band-title{font-family:"Bebas Neue",Impact,sans-serif;font-weight:400;color:var(--yellow);line-height:1;letter-spacing:.3px}
.dots{list-style:none;margin-left:6px}
.dots li{position:relative;padding-left:8px;font-size:7.2px;line-height:1.38}
.dots li::before{content:"";position:absolute;left:0;top:4px;width:3px;height:3px;border-radius:50%;background:var(--ink)}
.sub{font-size:7.4px;font-weight:700;margin-top:4px;margin-bottom:1px}
.brand-name{display:flex;align-items:center;justify-content:center;gap:6px;font-size:10px;font-weight:400;color:var(--navy)}
.brand-name i{display:block;width:12px;height:12px;border-radius:50%;background:var(--gold)}
</style>
</head>
<body>

<section class="sheet sheet--outer">

  <div class="panel panel--1">
    <div class="photo" role="img" aria-label="Jubelnde Jugendliche am Schreibtisch in einem hellen Zimmer" style="top:0;height:157px;background:linear-gradient(135deg,#eee9e2,#c9b8a6 55%,#8a6f5c)"></div>
    <h2 class="heading abs" style="left:16px;top:165px;font-size:21px">Vorteile und Nutzen</h2>
    <ul class="ticks abs" style="left:16px;top:188px;width:212px">
      <li><svg viewBox="0 0 10 9"><path d="M1 5l3 3 5-7" fill="none" stroke="#15126b" stroke-width="1.8"/></svg>Beste Prävention für die psychische Gesundheit, Steigerung des Wohlbefindens von Geist, Körper und Seele</li>
      <li><svg viewBox="0 0 10 9"><path d="M1 5l3 3 5-7" fill="none" stroke="#15126b" stroke-width="1.8"/></svg>Konkrete Lösungsansätze bei auftretenden Konflikten, Schulproblemen und Mobbing</li>
      <li><svg viewBox="0 0 10 9"><path d="M1 5l3 3 5-7" fill="none" stroke="#15126b" stroke-width="1.8"/></svg>Veränderter Umgang bzw. Reduktion von Überforderung, Leistungsdruck und Schulstress</li>
      <li><svg viewBox="0 0 10 9"><path d="M1 5l3 3 5-7" fill="none" stroke="#15126b" stroke-width="1.8"/></svg>Persönlichkeitsentwicklung, Lernen fürs Leben</li>
      <li><svg viewBox="0 0 10 9"><path d="M1 5l3 3 5-7" fill="none" stroke="#15126b" stroke-width="1.8"/></svg>Grundlagen zur Gestaltung eines glücklichen, erfolgreichen Lebens</li>
      <li><svg viewBox="0 0 10 9"><path d="M1 5l3 3 5-7" fill="none" stroke="#15126b" stroke-width="1.8"/></svg>Stärkung von Selbstbewusstsein, Selbstvertrauen, Selbstliebe und Selbstwert</li>
    </ul>
    <h2 class="heading abs" style="left:16px;top:374px;font-size:18px;line-height:1.05">Voraussetzungen für<br>die Teilnahme</h2>
    <div class="body abs" style="left:16px;top:413px;width:210px">
      <p>Das wichtigste ist, dass dein Kind am Lehrgang teilnehmen will.</p>
      <p>Interesse, Neugierde und vor allem die Bereitschaft zur aktiven Umsetzung der Inhalte sind notwendig, um gute Ergebnisse zu erzielen.</p>
    </div>
  </div>

  <div class="panel panel--2">
    <div class="abs" style="left:10px;top:14px;width:180px;height:50px;background:linear-gradient(90deg,var(--navy) 55%,#ffffff)"></div>
    <h2 class="band-title abs" style="left:16px;top:21px;font-size:18px">Kontakt &amp;<br>Veranstalterin:</h2>
    <div class="abs" style="left:14px;top:82px;font-size:13px;font-weight:700;color:var(--navy)">Mag. Helena Brunnthaler</div>
    <div class="abs" style="left:14px;top:100px;font-size:7.6px;color:var(--navy)">Selbstwert Coach, Bewusstseinstrainerin</div>
    <div class="abs" style="left:14px;top:127px;font-size:7.6px;color:var(--navy);line-height:1.55">
      <b>E-Mail :</b>&nbsp; info@innenkraft-staerken.at<br>
      <b>Mobil&nbsp; :</b>&nbsp; +43(0)650 482 3170
    </div>
    <svg class="abs" style="left:32px;top:187px" width="170" height="170" viewBox="0 0 170 170">
      <path d="M21 124 A75 75 0 1 1 124 149" fill="none" stroke="#15126b" stroke-width="5"/>
      <path d="M14 70 A72 72 0 0 0 120 151" fill="none" stroke="#f7c600" stroke-width="5" transform="translate(6 4)"/>
    </svg>
    <div class="abs" role="img" aria-label="Porträtfoto der Coachin" style="left:53px;top:208px;width:128px;height:128px;border-radius:50%;background:radial-gradient(circle at 50% 45%,#e8c7a8,#c9a069 60%,#8a8f6a)"></div>
    <div class="brand-name abs" style="left:0;width:100%;top:432px"><i></i>Helena Brunnthaler</div>
    <div class="gold-strip" style="bottom:0;height:9px"></div>
  </div>

  <div class="panel panel--3">
    <div class="photo" role="img" aria-label="Lachende junge Frau mit Locken und geballter Faust" style="top:0;height:243px;background:linear-gradient(160deg,#e8e4df,#c9a27a 45%,#8e6b4c)"></div>
    <div class="navy-band" style="top:193px;height:50px;background:linear-gradient(90deg,var(--navy) 70%,rgba(21,18,107,.6))"></div>
    <h1 class="band-title abs" style="left:13px;top:201px;font-size:19px">Innenkraft<br>Akademie <span style="font-family:'Open Sans',sans-serif;font-size:7.6px;letter-spacing:0">für Jugendliche ab 16</span></h1>
    <div class="gold-strip" style="top:243px;height:19px"></div>
    <div class="abs" style="left:16px;top:293px;width:205px;font-size:8.4px;line-height:1.45;color:#333">
      <p style="margin-bottom:9px">Schulbegleitender Praxis Lehrgang für<br>mentale Stärke und Selbstbewusstsein</p>
      <p style="margin-bottom:9px">Schulstress &amp; Leistungsdruck bewältigen<br>Selbstsicherer, gelassener &amp; angstfrei werden</p>
      <p>und dabei<br>ein starkes Selbstwertgefühl aufbauen<br>und sich selbst vertrauen</p>
    </div>
    <div class="gold-strip" style="top:435px;height:9px"></div>
    <div class="navy-band" style="top:444px;height:51px"></div>
    <p class="abs" style="left:16px;top:450px;width:205px;font-size:8px;font-style:italic;color:#fff;line-height:1.45">Einfache Übungen, Techniken und Methoden für den Alltag und ein glückliches erfolgreiches Leben</p>
  </div>
</section>

<section class="sheet sheet--inner">

  <div class="panel panel--1">
    <h2 class="heading abs" style="left:13px;top:18px;font-size:24px;line-height:1.16">Hast du das Gefühl,<br>deinem Kind wird<br>alles zu viel?</h2>
    <div class="body abs" style="left:13px;top:107px;width:212px">
      <p>Leidet auch dein Kind an Schulstress, Leistungsdruck und hat zu wenig Selbstbewusstsein?</p>
      <p>Das Jugendalter ist eine wichtige, oft schwierig verlaufende Entwicklungsphase, in der sich Jugendliche selbst erfahren und finden dürfen. Durch den stressigen, durch Leistungsdruck geprägten Schulalltag wird die Psyche doppelt gefordert. Viele Jugendliche fühlen sich schlecht, wissen oft nicht mehr weiter, negative Gedanken und Ängste machen sich breit. Oft geht der Glaube an sich selbst verloren. Das Selbstbewusstsein und der eigene Selbstwert schwinden.</p>
      <p>Ziel des begleitenden Coachings ist, die Jugendlichen zu befähigen, Herausforderungen des Lebens gut meistern und wieder Freude und Spaß am Leben empfinden zu können. Zu den Schwerpunkten zählt die Rückbesinnung auf sich selbst und die eigene Gefühlswelt, Persönlichkeitsentwicklung und die Anwendung der geistigen Gesetze.</p>
      <p>Der Lehrgang ist aktive Lebensschule, motiviert zur Freude an der Eigenverantwortung und Gestaltung eines glücklichen Lebens in körperlicher, geistiger und seelischer Gesundheit.</p>
    </div>
    <div class="photo" role="img" aria-label="Drei fröhliche junge Frauen in einem Sonnenblumenfeld" style="top:375px;height:120px;background:linear-gradient(180deg,#ffffff 0%,#f3e2a8 25%,#e8b42a 60%,#9c7a1e)"></div>
  </div>

  <div class="panel panel--2">
    <div class="photo" role="img" aria-label="Bücherstapel mit grünem Zitronenzweig" style="top:0;height:125px;background:linear-gradient(180deg,#f4f4f2,#dfe0da 60%,#b8bfa6)"></div>
    <div class="abs" style="left:0;top:125px;width:200px;height:30px;background:linear-gradient(90deg,var(--navy) 55%,#ffffff)"></div>
    <h2 class="abs" style="left:10px;top:126px;font-size:20px;font-weight:700;color:var(--yellow)">20 MODULE</h2>
    <div class="abs" style="left:8px;top:160px;width:218px">
      <p style="font-size:7.4px;line-height:1.42"><b>Innerhalb von 20 Modulen während des Schuljahres</b> werden einfache Übungen, Techniken und Methoden für den Alltag und die geistigen Lebensgesetze gelehrt und trainiert. Gemeinsam greifen wir Schwierigkeiten des täglichen Lebens auf und erarbeiten Lösungsmöglichkeiten.</p>
      <h3 style="font-size:9.5px;color:var(--navy);margin-top:5px">INHALTE</h3>
      <p class="sub">sich gut fühlen Dein Kind lernt,</p>
      <ul class="dots">
        <li>mit negativen Gedanken und Gefühlen umzugehen</li>
        <li>aus sich selbst Kraft und Energie zu tanken</li>
        <li>trotz Schulstress und Belastungen entspannt zu bleiben</li>
        <li>angstfreier und gelassener zu sein</li>
      </ul>
      <p class="sub">glücklich sein Dein Kind lernt,</p>
      <ul class="dots">
        <li>mit mentalen Bildern und Affirmationen zu arbeiten</li>
        <li>auf seine innere Stimme und sein Herz zu hören und zu vertrauen</li>
        <li>sein Leben glücklich und erfolgreich zu gestalten und zu erleben</li>
      </ul>
      <p class="sub">an sich glauben Dein Kind lernt,</p>
      <ul class="dots">
        <li>an sich und seine Fähigkeiten zu glauben und ein positives Bild von sich zu entwickeln</li>
        <li>selbstsicher, selbstbewusst und innerlich stark zu werden</li>
        <li>sich zu vertrauen und sich zutrauen, das zu sagen, was es denkt und fühlt, egal was Mitschüler/innen oder Freund/innen denken</li>
        <li>sich selbst zu mögen und sich so anzunehmen, wie es ist</li>
        <li>mit Konflikten umzugehen und Probleme schneller zu lösen</li>
      </ul>
    </div>
    <div class="gold-strip" style="bottom:0;height:9px"></div>
  </div>

  <div class="panel panel--3">
    <div class="photo" role="img" aria-label="Lächelnde Coachin mit blonden Haaren im Sonnenlicht" style="top:0;height:202px;background:linear-gradient(150deg,#3b3a7a,#c99a66 40%,#e8c7a0 70%,#f1e4cf)"></div>
    <div class="navy-band" style="top:154px;height:48px;background:linear-gradient(90deg,var(--navy) 70%,rgba(21,18,107,.55))"></div>
    <h2 class="band-title abs" style="left:13px;top:161px;font-size:19px">Die Coachin und<br>Vortragende</h2>
    <div class="body abs" style="left:8px;top:210px;width:220px;font-size:7.4px">
      <p><b>Helena Brunnthaler</b> leitet den schulbegleitenden Lehrgang Innenkraft Akademie. Sie ist gelernte Pädagogin für allgemeinbildende höhere Schulen für die Fächer Psychologie/Philosophie/Pädagogik und Bildnerische Erziehung. Als Selbstwert- und Selbstbewusstseins Coach, Mental- und Emotional Coach und Bewusstseinstrainerin begleitet sie seit 2006 Erwachsene und Jugendliche in ihrer Praxis sowie online.</p>
      <p>Sie zeigt Wege aus Krisen und vermittelt Tools und Werkzeug, das „Wie“ um das eigene Leben glücklich gestalten zu können</p>
      <h3 style="font-size:10px;color:var(--navy);margin:6px 0 3px">TERMINE</h3>
      <p>Die 20 Module finden alle 2 Wochen immer dienstags (18.00 – ca. 20.00 Uhr oder länger) schulbegleitend statt und können nur insgesamt gebucht werden. (Terminänderungen vorbehalten)Die aktuellen Termine und Kosten für den gesamten Lehrgang finden Sie unter:<br><b>https://www.innenkraft-staerken.at/innenkraft-akademie/</b></p>
    </div>
    <div class="navy-band" style="top:448px;height:47px"></div>
    <div class="abs" style="left:10px;top:458px;color:#fff">
      <div style="font-size:8.5px;font-weight:700">ORT</div>
      <div style="font-size:7.2px">Der Lehrgang findet online via MeetRaum statt.</div>
    </div>
  </div>
</section>

</body>
</html>
```